rk ironcraft business card metallic look

revamp the existing design but want card to have a metalic look to it

Target Market(s)

construction industry

Industry/Entity Type

constrction

Contact Information for Business Card

front of card RK Ironcraft, phone 4165550193, email rk.ironcraftt@veltrano.com and instagram account; rk_ironcraft_

Font styles to use
Other font styles liked:
• masculine

Colors

Designer to choose only greyscale colors for use in the design.

Requirements
Must have
• back side RK Ironcraft then a list of everything : Siding, ACM Panels, Standing Seam,Soffit, Fascia, Gutters,Metal,Alu,inum, Viynyl, Metal Roofs and roof repairs
Nice to have
• I would like to keep the look of the existing card with the metal grids on the front
Should not have
• Need a design in two days

```html
<!DOCTYPE html>
<html lang="en">
<head>
<meta charset="UTF-8">
<title>RK Ironcraft Business Card</title>
<link href="https://fonts.googleapis.com/css2?family=Lato:wght@400;700&display=swap" rel="stylesheet">
<style>
  :root {
    --backdrop: #e6e6e6;
    --white: #ffffff;
    --ink-light: #f2f2f2;
    --icon-ink: #222222;
    --steel-black: #050505;
    --card-shadow: rgba(0, 0, 0, 0.25);
  }
  * { margin: 0; padding: 0; box-sizing: border-box; }
  html, body { width: 1098px; height: 1200px; overflow: hidden; }
  body {
    background: var(--backdrop);
    font-family: "Lato", Arial, sans-serif;
    position: relative;
  }
  .card {
    position: absolute;
    left: 169px;
    width: 760px;
    height: 436px;
    overflow: hidden;
    box-shadow: 0 4px 14px var(--card-shadow);
  }
  .card--front {
    top: 120px;
    background: linear-gradient(180deg,
      #1a1a1a 0%, #4f4f4f 16%, #9c9c9c 30%, #2a2a2a 44%,
      var(--steel-black) 54%, #5e5e5e 68%, #dcdcdc 79%,
      #8c8c8c 91%, #4a4a4a 100%);
  }
  .card--back {
    top: 644px;
    background: linear-gradient(180deg,
      #3a3a3a 0%, #8a8a8a 18%, #bdbdbd 28%, #2b2b2b 40%,
      var(--steel-black) 50%, #3c3c3c 60%, #d4d4d4 77%,
      #9a9a9a 88%, #555555 100%);
  }
  .block { position: absolute; background: var(--white); }
  .grid-bar {
    position: absolute;
    background: linear-gradient(180deg, var(--white) 0%, var(--white) 60%, rgba(255,255,255,0.55) 100%);
  }
  .grid-bar--base { background: var(--white); }

  .brand-name {
    position: absolute;
    left: 60px;
    top: 250px;
    width: 230px;
    text-align: center;
    font-weight: 700;
    font-size: 32px;
    color: var(--ink-light);
    letter-spacing: 0.5px;
  }
  .divider {
    position: absolute;
    left: 300px;
    top: 205px;
    width: 2px;
    height: 133px;
    background: var(--ink-light);
  }
  .contact-list {
    position: absolute;
    left: 320px;
    top: 224px;
    list-style: none;
  }
  .contact-item {
    display: flex;
    align-items: center;
    height: 31px;
    font-size: 23px;
    color: var(--white);
  }
  .contact-icon {
    width: 22px;
    height: 22px;
    margin-right: 16px;
    flex: none;
  }
  .back-name {
    position: absolute;
    left: 0;
    top: 180px;
    width: 760px;
    text-align: center;
    font-weight: 700;
    font-size: 26px;
    color: var(--ink-light);
    letter-spacing: 0.5px;
  }
  .services {
    position: absolute;
    left: 0;
    top: 232px;
    width: 760px;
    text-align: center;
    font-size: 18.5px;
    line-height: 34px;
    color: var(--white);
    text-transform: uppercase;
  }
  .services strong { font-weight: 700; }
</style>
</head>
<body>

  <section class="card card--front" aria-label="Card front">
    <div class="block" style="left:0;top:0;width:300px;height:157px;"></div>
    <div class="grid-bar" style="left:310px;top:0;width:17px;height:157px;"></div>
    <div class="grid-bar" style="left:344px;top:0;width:17px;height:157px;"></div>
    <div class="grid-bar" style="left:378px;top:0;width:17px;height:157px;"></div>

    <div class="brand-name">RK Ironcraft</div>
    <div class="divider"></div>

    <ul class="contact-list">
      <li class="contact-item">
        <svg class="contact-icon" viewBox="0 0 24 24" aria-hidden="true">
          <rect x="2" y="5" width="20" height="14" rx="1.5" fill="#fff"/>
          <path d="M3 6.5 L12 13 L21 6.5" fill="none" stroke="#222" stroke-width="2"/>
        </svg>
        rk.ironcraftt@veltrano.com
      </li>
      <li class="contact-item">
        <svg class="contact-icon" viewBox="0 0 24 24" aria-hidden="true">
          <circle cx="12" cy="12" r="11" fill="#fff"/>
          <circle cx="12" cy="12" r="3.2" fill="none" stroke="#222" stroke-width="1.8"/>
          <path d="M15.2 9.5v3.6c0 1.4 2.6 1.6 2.8-.6.4-3.6-2.3-6.4-5.8-6.2-3.2.2-5.6 2.9-5.4 6.1.2 3.3 3.3 5.6 6.6 5" fill="none" stroke="#222" stroke-width="1.8" stroke-linecap="round"/>
        </svg>
        rk_ironcraft_
      </li>
      <li class="contact-item">
        <svg class="contact-icon" viewBox="0 0 24 24" aria-hidden="true">
          <circle cx="12" cy="12" r="11" fill="#fff"/>
          <path d="M8.2 6.5c.5-.4 1.1-.3 1.4.2l1.1 1.9c.3.5.2 1-.2 1.4l-.8.7c.7 1.5 1.9 2.8 3.4 3.6l.8-.8c.4-.4 1-.4 1.4-.1l1.8 1.2c.5.3.6 1 .2 1.4l-.9 1c-.6.6-1.5.8-2.3.5-3.3-1.2-5.9-3.9-7-7.2-.3-.8 0-1.7.6-2.3z" fill="#222"/>
        </svg>
        416 555 0193
      </li>
    </ul>

    <div class="grid-bar grid-bar--base" style="left:164px;top:379px;width:22px;height:57px;"></div>
    <div class="grid-bar grid-bar--base" style="left:207px;top:379px;width:22px;height:57px;"></div>
    <div class="grid-bar grid-bar--base" style="left:250px;top:379px;width:22px;height:57px;"></div>
    <div class="block" style="left:290px;top:379px;width:470px;height:57px;"></div>
  </section>

  <section class="card card--back" aria-label="Card back">
    <div class="block" style="left:0;top:0;width:611px;height:158px;"></div>
    <div class="grid-bar" style="left:617px;top:0;width:17px;height:158px;"></div>
    <div class="grid-bar" style="left:654px;top:0;width:17px;height:158px;"></div>
    <div class="grid-bar" style="left:692px;top:0;width:17px;height:158px;"></div>
    <div class="grid-bar" style="left:728px;top:0;width:17px;height:158px;"></div>

    <div class="back-name">RK Ironcraft</div>

    <p class="services">
      Siding| <strong>ACM Panels</strong>| Standing Seam| Soffit| Fascia| Gutters| Metal| Alu<br>
      inum| Viynyl |Metal Roofs | Roof Repairs
    </p>

    <div class="grid-bar grid-bar--base" style="left:23px;top:377px;width:22px;height:59px;"></div>
    <div class="grid-bar grid-bar--base" style="left:64px;top:377px;width:22px;height:59px;"></div>
    <div class="grid-bar grid-bar--base" style="left:107px;top:377px;width:22px;height:59px;"></div>
    <div class="block" style="left:151px;top:377px;width:609px;height:59px;"></div>
  </section>

</body>
</html>
```